"Hushwell Chews" is the brand name for CBN infused Gummies for a restful sleep

Need a label for the glass jar and a round label for the lid. The gummy shapes are crescent white mons and blue stars or gummy sheep

You can use an 6 or 8 oz clear jar. Your illustration program should have this mock up.

Font styles to use
Sans Serif

```html
<!DOCTYPE html>
<html lang="en">
<head>
<meta charset="utf-8">
<title>Hushwell Chews – Jar and Lid Labels</title>
<link rel="stylesheet" href="https://fonts.googleapis.com/css2?family=Dosis:wght@400;500;600&display=swap">
<style>
  :root {
    --page: #ffffff;
    --night-top: #1b1f4a;
    --night-mid: #262a5e;
    --night-deep: #12143a;
    --gold: #dccb93;
    --amber: #e3ae52;
    --rule-blue: #3f74a8;
    --line: #c9c9d6;
    --ink-light: #e6e6ee;
  }
  * { box-sizing: border-box; margin: 0; padding: 0; }
  html, body { width: 1200px; height: 772px; overflow: hidden; background: var(--page); }
  body { position: relative; font-family: "Dosis", sans-serif; }

  .jar-label {
    position: absolute; left: 90px; top: 156px; width: 640px; height: 460px;
    background: linear-gradient(180deg, var(--night-deep) 0%, var(--night-top) 45%, var(--night-mid) 100%);
    display: flex; flex-direction: column; align-items: center;
  }
  .jar-label__sky {
    position: absolute; inset: 0;
    background: radial-gradient(ellipse at 50% 20%, rgba(255,255,255,0.06), rgba(255,255,255,0) 60%);
  }
  .brand-name {
    margin-top: 92px; font-size: 92px; font-weight: 400; color: var(--gold);
    line-height: 1; letter-spacing: 1px; position: relative;
  }
  .brand-rule {
    width: 320px; height: 5px; border-radius: 3px; background: var(--rule-blue);
    margin-top: 10px; position: relative;
  }
  .product-line {
    margin-top: 8px; font-size: 22px; font-weight: 500; color: var(--amber);
    letter-spacing: 0.5px; position: relative;
  }
  .facts {
    display: flex; margin-top: 30px; border: 1.5px solid var(--line); position: relative;
  }
  .facts__cell {
    width: 118px; height: 66px; display: flex; flex-direction: column; align-items: center; justify-content: center;
    color: var(--ink-light); font-size: 16px; letter-spacing: 1px; line-height: 1.2; text-align: center;
  }
  .facts__cell + .facts__cell { border-left: 1.5px solid var(--line); }
  .facts__cell--count .facts__big { font-size: 24px; }
  .flavor-note { margin-top: 14px; font-size: 16px; color: var(--ink-light); letter-spacing: 1.5px; position: relative; }
  .badge {
    margin-top: 26px; width: 44px; height: 44px; border-radius: 50%;
    border: 1.5px solid var(--gold); position: relative;
  }

  .lid-label {
    position: absolute; left: 790px; top: 216px; width: 340px; height: 340px; border-radius: 50%;
    background: radial-gradient(circle at 50% 40%, var(--night-mid) 0%, var(--night-deep) 100%);
    border: 10px solid #111;
    display: flex; flex-direction: column; align-items: center; justify-content: center;
  }
  .lid-label .brand-name { margin-top: 0; font-size: 64px; }
  .lid-label .brand-rule { width: 200px; height: 4px; }
  .lid-label .product-line { font-size: 16px; color: var(--ink-light); }
  .lid-label .badge { margin-top: 18px; width: 30px; height: 30px; }
</style>
</head>
<body>
  <section class="jar-label" aria-label="Jar label">
    <div class="jar-label__sky" role="img" aria-label="Night sky with scattered stars"></div>
    <h1 class="brand-name">Hushwell</h1>
    <div class="brand-rule"></div>
    <p class="product-line">GUMMIES INFUSED WITH CBN</p>
    <div class="facts">
      <div class="facts__cell facts__cell--count"><span class="facts__big">30</span><span>GUMMIES</span></div>
      <div class="facts__cell"><span>SLEEP</span><span>RELIEF</span></div>
      <div class="facts__cell"><span>20MG CBN</span><span>/PACKAGE</span></div>
    </div>
    <p class="flavor-note">NATURAL FLAVORED</p>
    <div class="badge"></div>
  </section>

  <section class="lid-label" aria-label="Lid label">
    <h2 class="brand-name">Hushwell</h2>
    <div class="brand-rule"></div>
    <p class="product-line">GUMMIES INFUSED WITH CBN</p>
    <div class="badge"></div>
  </section>
</body>
</html>
```